Corvane Lending Partners - Real estate loans - need a business card with a logo

I need a logo and a business card that looks elegant - that looks as if it is a big stablish corporation - We do real estate loans, my goal is to brand myself with colors black background - gold or silver letters - some combination - Name of the company different color than the rest of the card -

```html
<!DOCTYPE html>
<html lang="en">
<head>
<meta charset="utf-8">
<title>Corvane Lending Partners – Business Card</title>
<link rel="stylesheet" href="https://fonts.googleapis.com/css2?family=Poppins:wght@400;500;600&display=swap">
<style>
  :root {
    --page: #1d1e22;
    --card: #202326;
    --card-edge: #2a2d31;
    --gold: #c9a447;
    --gold-light: #e2c56c;
    --silver: #b9bcc0;
    --white: #f2f2f2;
  }
  * { margin: 0; padding: 0; box-sizing: border-box; }
  html, body {
    width: 1200px; height: 800px; overflow: hidden;
    background: var(--page);
    font-family: "Poppins", sans-serif;
  }
  .canvas {
    width: 1200px; height: 800px;
    display: flex; align-items: center; justify-content: center; gap: 48px;
  }
  .card {
    width: 520px; height: 300px;
    background: var(--card);
    border: 1px solid var(--card-edge);
    border-radius: 22px;
    box-shadow: 0 20px 40px rgba(0,0,0,.45);
    position: relative;
    overflow: hidden;
  }
  /* front */
  .card-front {
    display: flex; align-items: center; justify-content: center;
  }
  .wordmark {
    text-align: center;
    font-weight: 500;
    text-transform: uppercase;
    line-height: 1.5;
  }
  .wordmark-main { display: block; font-size: 30px; letter-spacing: 9px; }
  .wordmark-sub { display: block; font-size: 12px; letter-spacing: 7px; }
  .card-front .wordmark { color: var(--silver); }
  /* back */
  .card-back { display: flex; align-items: center; }
  .card-back .brand {
    width: 250px; display: flex; justify-content: center;
  }
  .card-back .wordmark { color: var(--gold-light); }
  .card-back .wordmark-main { font-size: 20px; letter-spacing: 5px; }
  .card-back .wordmark-sub { font-size: 9px; letter-spacing: 4px; }
  .divider {
    width: 1px; height: 150px;
    background: linear-gradient(var(--card), var(--gold), var(--card));
  }
  .contact { padding-left: 28px; color: var(--white); }
  .person-name {
    color: var(--gold); font-weight: 600; font-size: 19px; letter-spacing: .5px;
    text-transform: uppercase; line-height: 1.1;
  }
  .person-role {
    font-size: 9px; font-weight: 500; letter-spacing: 1px;
    text-transform: uppercase; margin-bottom: 16px;
  }
  .address { font-size: 11.5px; line-height: 1.45; margin-bottom: 12px; }
  .contact-list { list-style: none; font-size: 11.5px; line-height: 1.7; }
  .contact-list li { display: flex; align-items: center; gap: 8px; }
  .contact-list svg { width: 11px; height: 11px; flex: none; }
</style>
</head>
<body>
<main class="canvas">
  <section class="card card-front" aria-label="Card front">
    <div class="wordmark">
      <span class="wordmark-main">Corvane</span>
      <span class="wordmark-sub">Lending Partners</span>
    </div>
  </section>

  <section class="card card-back" aria-label="Card back">
    <div class="brand">
      <div class="wordmark">
        <span class="wordmark-main">Corvane</span>
        <span class="wordmark-sub">Lending Partners</span>
      </div>
    </div>
    <div class="divider"></div>
    <div class="contact">
      <p class="person-name">Elias Harwood</p>
      <p class="person-role">Director</p>
      <p class="address">PO Box 418, Harbour Lane<br>12 Kestrel Street, Ashford</p>
      <ul class="contact-list">
        <li>
          <svg viewBox="0 0 24 24" aria-hidden="true"><path fill="#c9a447" d="M6.6 10.8a15.2 15.2 0 0 0 6.6 6.6l2.2-2.2c.3-.3.7-.4 1-.2 1.1.4 2.3.6 3.6.6.6 0 1 .4 1 1V20c0 .6-.4 1-1 1A17 17 0 0 1 3 4c0-.6.4-1 1-1h3.5c.6 0 1 .4 1 1 0 1.3.2 2.5.6 3.6.1.3 0 .7-.2 1z"/></svg>
          +1 555 014 2290
        </li>
        <li>
          <svg viewBox="0 0 24 24" aria-hidden="true"><rect x="2" y="5" width="20" height="14" rx="1.5" fill="#c9a447"/><path d="M2.5 6l9.5 7 9.5-7" fill="none" stroke="#202326" stroke-width="1.6"/></svg>
          hello@corvanelending.com
        </li>
        <li>
          <svg viewBox="0 0 24 24" aria-hidden="true"><g fill="none" stroke="#c9a447" stroke-width="2"><circle cx="12" cy="12" r="9.5"/><ellipse cx="12" cy="12" rx="4.2" ry="9.5"/><path d="M2.5 12h19M4 7h16M4 17h16"/></g></svg>
          www.corvanelending.com
        </li>
      </ul>
    </div>
  </section>
</main>
</body>
</html>
```